Website Design for a New Business Sharing Application

Purpose: Website for a new product – a sharing application called "Pondly.io"

Product concept: Easy sharing of business information. The application has different sections: tasks, calendars, documents, contacts, notes and links. The key feature of the application is that you can drag and drop information from different sections into a "share." A share is a page which lists all the types of information that you drag into it. You can add people to this "share."

Note: The application itself is not part of this project, just the website.

Website details: The site, in addition to being informational, will actually be the first point of entry for visitors into the application itself. Because of that, we would like the website design to reflect the look of the application, to create a smooth and seamless experience for the user moving from the website into the application (tough the website does not need to look *exactly* like the application). Included Product Tour screenshots show you the look of the application.

Website pages to be created: 4 pages
We are flexible in terms of the exact structure and placement of elements. You may change that any way you like. The pages are as follows:

Home page
Product Tour page
Press page
Blog page

Specific description of pages are provided in project files we will upload. We will also upload the logo, home page layout we have in mind, and other supporting files.

NOTE: Please submit first the design of the home page. Based on this design we will ask selected designers to submit designs for the other pages.

Target Market(s)

Business people who want to share work related files with their colleagues

Industry/Entity Type

Business

Requirements
Must have
• All the required features are listed in the description of the website and specific pages that we will upload.

```html
<!DOCTYPE html>
<html lang="en">
<head>
<meta charset="utf-8">
<title>Pondly.io — Drag Files. Add People.</title>
<link rel="stylesheet" href="https://fonts.googleapis.com/css2?family=Open+Sans:wght@400;600;700&family=Gochi+Hand&family=Kaushan+Script&display=swap">
<style>
  :root {
    --topbar: #262626;
    --topbar-text: #bdbdbd;
    --panel: rgba(30, 30, 30, 0.72);
    --white: #ffffff;
    --script-blue: #3fb0e0;
    --dropzone: #d4d4d4;
    --dropzone-edge: #bcbcbc;
    --dropzone-text: #8c8c8c;
    --input-bg: #ececec;
    --input-text: #9a9a9a;
    --button-top: #fbd56a;
    --button-bottom: #f4b83c;
    --button-text: #4a3a12;
    --card: #e7e7e7;
    --card-inner: #e2e2e2;
    --card-line: #cfcfcf;
    --label: #555555;
    --heading: #555555;
    --link-blue: #2a8fd0;
    --video: #b3b3b3;
    --video-bar: #2c2c2c;
    --page: #f4f4f4;
    --footer: #e3e3e3;
    --footer-text: #333333;
    --ink: #1e1e1e;
    --green: #5cb043;
    --teal: #4fb4d4;
    --red: #c6605a;
    --purple: #9a6ec2;
    --yellow: #e5c63c;
    --blue: #2f86c2;
    --pink: #d25ccd;
    --grey: #8f8f8f;
    --orange: #e9883a;
  }
  * { margin: 0; padding: 0; box-sizing: border-box; }
  html, body { width: 1200px; height: 675px; overflow: hidden; }
  body {
    position: relative;
    background: var(--page);
    font-family: "Open Sans", Arial, sans-serif;
  }
  .abs { position: absolute; }

  /* top bar */
  .topbar { left: 0; top: 0; width: 1200px; height: 44px; background: var(--topbar); }
  .brand { left: 187px; top: 9px; display: flex; align-items: center; gap: 7px;
    color: var(--white); font-weight: 700; font-size: 17px; }
  .brand-dot { width: 18px; height: 18px; border-radius: 50%; background: var(--orange); }
  .social { top: 13px; width: 17px; height: 17px; background: #7a7a7a; border-radius: 2px; }
  .access { left: 904px; top: 15px; color: var(--topbar-text); font-size: 11.5px; }

  /* hero */
  .hero-photo { left: 0; top: 44px; width: 1200px; height: 397px;
    background:
      radial-gradient(ellipse 220px 260px at 60px 160px, #c2305e 0%, transparent 70%),
      radial-gradient(ellipse 260px 200px at 420px 60px, #e0c020 0%, transparent 70%),
      radial-gradient(ellipse 260px 240px at 640px 300px, #d14a1e 0%, transparent 70%),
      radial-gradient(ellipse 240px 260px at 880px 120px, #7b2f8e 0%, transparent 70%),
      radial-gradient(ellipse 240px 280px at 1150px 200px, #2f5fb8 0%, transparent 70%),
      radial-gradient(ellipse 260px 200px at 300px 360px, #2d8c4a 0%, transparent 70%),
      linear-gradient(90deg, #7a1f3c, #b86a20, #5a2a72, #1f3f8a);
  }
  .hero-panel { left: 172px; top: 48px; width: 861px; height: 303px; background: var(--panel); }
  .script { font-family: "Gochi Hand", cursive; color: var(--script-blue); }
  .tagline { left: 198px; top: 50px; font-size: 18px; line-height: 17px; transform: rotate(-2deg); }
  .headline { left: 186px; color: var(--white); font-weight: 700; font-size: 47px;
    letter-spacing: -0.5px; line-height: 1; }
  .headline.first { top: 84px; }
  .headline.second { top: 137px; }
  .headline.boom { top: 190px;
    background: linear-gradient(90deg, #e45a8a, #f0b040, #6cc08a, #5a9ad8);
    -webkit-background-clip: text; background-clip: text; color: transparent; }
  .social-note { left: 399px; top: 187px; font-size: 16px; transform: rotate(-8deg); }
  .intro { left: 187px; top: 251px; width: 410px; color: var(--white);
    font-size: 14px; line-height: 22px; }
  .start-now { left: 492px; top: 312px; font-size: 21px; transform: rotate(-9deg); }
  .start-arrow { left: 574px; top: 306px; }

  /* drop zone */
  .dropzone { left: 610px; top: 72px; width: 400px; height: 163px; background: var(--dropzone);
    border: 1px solid var(--dropzone-edge);
    box-shadow: inset 0 3px 10px rgba(0,0,0,0.28), inset 0 -1px 3px rgba(0,0,0,0.12); }
  .drop-text { width: 100%; text-align: center; color: var(--dropzone-text); font-size: 12.5px; }
  .drop-text.line1 { top: 20px; }
  .drop-text.line2 { top: 46px; }
  .drop-plus { left: 161px; top: 74px; }

  .or { left: 794px; top: 243px; font-family: "Kaushan Script", cursive; color: var(--white);
    font-size: 34px; }
  .or-line { top: 266px; height: 1px; width: 150px; }
  .or-line.left { left: 630px; background: linear-gradient(90deg, transparent, rgba(255,255,255,0.35)); }
  .or-line.right { left: 852px; background: linear-gradient(90deg, rgba(255,255,255,0.35), transparent); }

  .email { left: 610px; top: 297px; width: 262px; height: 45px; background: var(--input-bg);
    border: 1px solid #cfcfcf; color: var(--input-text); font-size: 17px; padding: 11px 10px; }
  .start-btn { left: 872px; top: 297px; width: 140px; height: 45px;
    background: linear-gradient(var(--button-top), var(--button-bottom));
    border: 1px solid #d9a336; color: var(--button-text); font-size: 17px;
    text-align: center; line-height: 43px; }

  /* share card */
  .card { left: 172px; top: 365px; width: 861px; height: 265px; background: var(--card);
    box-shadow: 0 -2px 8px rgba(0,0,0,0.25); }
  .card-inner { left: 186px; top: 376px; width: 827px; height: 224px; background: var(--card-inner);
    border: 1px solid var(--card-line); }
  .stripe { left: 186px; top: 376px; width: 827px; height: 5px; display: flex; }
  .stripe span { flex: 1; }
  .card-title { left: 199px; top: 396px; color: var(--heading); font-weight: 600; font-size: 15px; }
  .item { display: flex; align-items: center; gap: 10px; color: var(--label); font-size: 13px; }
  .item-icon { width: 35px; height: 35px; border-radius: 2px; display: flex;
    align-items: center; justify-content: center; }
  .item.more { color: var(--link-blue); }
  .divider { left: 608px; top: 405px; width: 1px; height: 180px;
    background: linear-gradient(transparent, #b0b0b0 20%, #b0b0b0 80%, transparent); }

  .video { left: 629px; top: 427px; width: 367px; height: 151px; background: var(--video); }
  .video-bar { left: 0; bottom: 0; width: 100%; height: 24px; background: var(--video-bar); }

  /* footer */
  .free-note { left: 522px; top: 599px; font-family: "Gochi Hand", cursive; color: var(--ink);
    font-size: 18px; transform: rotate(-4deg); }
  .free-arrow { left: 503px; top: 614px; }
  .footer { left: 0; top: 630px; width: 1200px; height: 45px; background: var(--footer);
    border-top: 1px solid #d0d0d0; }
  .footer-nav { width: 100%; top: 16px; display: flex; justify-content: center; gap: 19px;
    color: var(--footer-text); font-size: 12px; }
  .footer-nav .struck { text-decoration: line-through; }
</style>
</head>
<body>

  <header class="abs topbar">
    <div class="abs brand"><span class="brand-dot"></span>Pondly.io</div>
    <span class="abs social" style="left:316px"></span>
    <span class="abs social" style="left:341px"></span>
    <span class="abs social" style="left:366px"></span>
    <div class="abs access">Access Your Files &#9656;</div>
  </header>

  <div class="abs hero-photo" role="img" aria-label="Close-up photograph of brightly coloured feathers in pink, yellow, orange, purple and blue"></div>
  <section class="abs hero-panel"></section>

  <div class="abs script tagline">Certified Fastest Sharing<br>In The Market!</div>
  <h1 class="abs headline first">Drag Files.</h1>
  <div class="abs headline second">Add People.</div>
  <div class="abs headline boom">Boom.</div>
  <div class="abs script social-note">It's social!</div>
  <p class="abs intro">Sharing with friends is simple, fast &amp; fun. Pondly.io brings the same ease to sharing with a partner, a contact at another company, a freelancer, a team-member OR a friend.</p>
  <div class="abs script start-now">Start Now</div>
  <svg class="abs start-arrow" width="26" height="16" viewBox="0 0 26 16">
    <path d="M2 13 Q12 14 21 5" fill="none" stroke="#3fb0e0" stroke-width="2.2" stroke-linecap="round"/>
    <path d="M15 4 L22 4 L21 11" fill="none" stroke="#3fb0e0" stroke-width="2.2" stroke-linecap="round" stroke-linejoin="round"/>
  </svg>

  <div class="abs dropzone">
    <div class="abs drop-text line1">Drag File Here</div>
    <div class="abs drop-text line2">To Share Immediately</div>
    <svg class="abs drop-plus" width="76" height="76" viewBox="0 0 76 76">
      <path d="M26 1 H50 V26 H75 V50 H50 V75 H26 V50 H1 V26 H26 Z" fill="#d0d0d0" stroke="#a9a9a9" stroke-width="1.5"/>
      <path d="M27 3 H49 V27 H73" fill="none" stroke="#f0f0f0" stroke-width="1"/>
    </svg>
  </div>

  <span class="abs or-line left"></span>
  <span class="abs or-line right"></span>
  <div class="abs or">Or</div>

  <div class="abs email">Enter Business Email</div>
  <div class="abs start-btn">Start Sharing</div>

  <section class="abs card"></section>
  <div class="abs card-inner"></div>
  <div class="abs stripe">
    <span style="background:#3a8fc8"></span><span style="background:#e6a272"></span>
    <span style="background:#d58a9c"></span><span style="background:#79c46a"></span>
    <span style="background:#5fc2dc"></span><span style="background:#d8756a"></span>
    <span style="background:#b795cf"></span><span style="background:#e0cf5c"></span>
    <span style="background:#4a9ad4"></span><span style="background:#d48fd0"></span>
  </div>
  <h2 class="abs card-title">Things to share:</h2>

  <div class="abs item" style="left:202px;top:430px"><span class="item-icon" style="background:var(--green)"><svg width="18" height="18" viewBox="0 0 18 18"><path d="M9 2v14M2 9h14" stroke="#fff" stroke-width="3"/></svg></span>Tasks</div>
  <div class="abs item" style="left:202px;top:470px"><span class="item-icon" style="background:var(--teal)"><svg width="18" height="18" viewBox="0 0 18 18"><path d="M9 2v14M2 9h14" stroke="#fff" stroke-width="3"/></svg></span>Contacts</div>
  <div class="abs item" style="left:202px;top:510px"><span class="item-icon" style="background:var(--red)"><svg width="18" height="18" viewBox="0 0 18 18"><path d="M9 2v14M2 9h14" stroke="#fff" stroke-width="3"/></svg></span>Links</div>
  <div class="abs item" style="left:202px;top:551px"><span class="item-icon" style="background:var(--purple)"><svg width="18" height="18" viewBox="0 0 18 18"><path d="M9 2v14M2 9h14" stroke="#fff" stroke-width="3"/></svg></span>Event</div>
  <div class="abs item" style="left:382px;top:430px;gap:24px"><span class="item-icon" style="background:var(--yellow)"><svg width="18" height="18" viewBox="0 0 18 18"><path d="M9 2v14M2 9h14" stroke="#fff" stroke-width="3"/></svg></span>Notes</div>
  <div class="abs item" style="left:382px;top:470px;gap:24px"><span class="item-icon" style="background:var(--blue)"><svg width="18" height="18" viewBox="0 0 18 18"><path d="M9 2v14M2 9h14" stroke="#fff" stroke-width="3"/></svg></span>Reminders</div>
  <div class="abs item" style="left:382px;top:510px;gap:24px"><span class="item-icon" style="background:var(--pink)"><svg width="18" height="18" viewBox="0 0 18 18"><path d="M9 2v14M2 9h14" stroke="#fff" stroke-width="3"/></svg></span>Documents</div>
  <div class="abs item more" style="left:382px;top:551px;gap:24px"><span class="item-icon" style="background:var(--grey)"><svg width="18" height="18" viewBox="0 0 18 18"><path d="M9 2v14M2 9h14" stroke="#fff" stroke-width="3"/></svg></span>And More</div>

  <div class="abs divider"></div>

  <div class="abs video">
    <svg class="abs" style="left:132px;top:18px" width="130" height="82" viewBox="0 0 130 82">
      <circle cx="45" cy="43" r="40" fill="none" stroke="#2e2e2e" stroke-width="4"/>
      <circle cx="45" cy="43" r="5" fill="none" stroke="#2e2e2e" stroke-width="3"/>
      <circle cx="45" cy="21" r="11" fill="#2e2e2e"/>
      <circle cx="45" cy="65" r="11" fill="#2e2e2e"/>
      <circle cx="23" cy="43" r="11" fill="#2e2e2e"/>
      <circle cx="67" cy="43" r="11" fill="#2e2e2e"/>
      <path d="M80 62 Q92 90 122 78" fill="none" stroke="#2e2e2e" stroke-width="4"/>
    </svg>
    <div class="abs video-bar">
      <svg class="abs" style="left:10px;top:6px" width="12" height="13" viewBox="0 0 12 13"><path d="M1 0 L12 6.5 L1 13 Z" fill="#e8e8e8"/></svg>
      <span class="abs" style="left:40px;top:10px;width:287px;height:5px;border-radius:3px;background:#e6e6e6"></span>
      <svg class="abs" style="left:336px;top:5px" width="20" height="14" viewBox="0 0 20 14"><path d="M1 4h4l5-4v14l-5-4H1z" fill="#e8e8e8"/><path d="M13 3q3 4 0 8M16 1q5 6 0 12" fill="none" stroke="#e8e8e8" stroke-width="1.5"/></svg>
    </div>
  </div>

  <div class="abs free-note">Free for unlimited users!</div>
  <svg class="abs free-arrow" width="18" height="18" viewBox="0 0 18 18">
    <path d="M14 2 Q6 4 7 15" fill="none" stroke="#1e1e1e" stroke-width="1.8" stroke-linecap="round"/>
    <path d="M3 11 L7 16 L11 11" fill="none" stroke="#1e1e1e" stroke-width="1.8" stroke-linecap="round"/>
  </svg>

  <footer class="abs footer">
    <nav class="abs footer-nav">
      <span>Home</span><span>About Us</span><span>Product Tour</span><span class="struck">Pricing</span>
      <span>Terms Of Use</span><span>Jobs</span><span>Sign Up</span><span>Blog</span><span>Press</span><span>Contact Us</span>
    </nav>
  </footer>

</body>
</html>
```